Brennick Framing Company - Card Design

I am looking to use the logo designs that you already did for me to develop a business card. I would like the card to have a black background and be double sided. I want white and green logo and text. I have attached an inspiration photo of a look that I like. I would like to use the Vertical Logo attached to take up the full front side of the card. On the back where I have my name and information, I would like to have the horizontal logo or maybe even just the image of the 'A' and trees without the text. I am open, but I am looking for something clean and simple and I want the green to really pop! Additional files can be found under Design #: 64093528

Target Market(s)

Homeowners

Industry/Entity Type

Construction

Contact Information for Business Card

Name: Marcus Brennick, Title: Project Manager, Phone: 647.382.9105, Email: brennickframingcompany@quillpost.example, address: 418 Larkspur Ln, Alder Bay, OR 97999, Lic# 5836214

Colors
00AB8E
00BBA5
67D7C9
C6EFE9
E9F9F6

Requirements
Nice to have
• I would like to see the logos that I have already got from ArtSwarm, though I am open to new ones

```html
<!DOCTYPE html>
<html lang="en">
<head>
<meta charset="utf-8">
<title>Brennick Framing Company – Business Cards</title>
<link href="https://fonts.googleapis.com/css2?family=Lato:wght@400;700;900&display=swap" rel="stylesheet">
<style>
  :root{
    --green:#70b548;
    --ink:#231f20;
    --white:#ffffff;
    --soft:#e6e6e6;
    --page:#ffffff;
  }
  *{margin:0;padding:0;box-sizing:border-box}
  html,body{width:1200px;height:1200px;overflow:hidden;background:var(--page)}
  body{position:relative;font-family:'Lato',sans-serif;color:var(--soft)}
  .card{position:absolute;background:var(--ink);overflow:hidden}
  .card--front-one{left:216px;top:89px;width:357px;height:594px}
  .card--front-two{left:627px;top:89px;width:357px;height:594px}
  .card--back{left:312px;top:756px;width:575px;height:344px}

  .hero-band{position:absolute;left:0;top:0;width:100%;height:305px;background:var(--green)}
  .hero-band__name{position:absolute;left:0;right:0;top:128px;text-align:center;
    font-weight:900;font-size:26px;letter-spacing:2px;line-height:1.2;color:var(--ink);text-transform:uppercase}

  .info{position:absolute;left:0;right:0;text-align:center}
  .info__name{font-weight:700;font-size:27px;letter-spacing:.3px;line-height:1;text-transform:uppercase}
  .info__title{font-size:18.5px;line-height:1;margin-top:8px;letter-spacing:.3px}
  .info__icons{display:flex;align-items:center;justify-content:center;gap:5px;margin:18px auto 0;width:278px}
  .info__rule{flex:1;height:1.5px;background:var(--green)}
  .info__icons svg{width:26px;height:26px;display:block}
  .info__icons .info__rule:first-child{margin-right:6px}
  .info__icons .info__rule:last-child{margin-left:6px}
  .info__phone{font-size:21px;letter-spacing:1px;margin-top:18px;line-height:1}
  .info__line{font-size:14.6px;letter-spacing:.4px;margin-top:7px;line-height:1.15}
  .info__divider{height:1.5px;background:var(--green);margin:0 auto}
  .info__lic{font-size:15px;letter-spacing:.5px;line-height:1}

  .card--front-one .info{top:315px}
  .card--front-one .info__name{color:var(--white)}
  .card--front-one .info__title{color:var(--green)}
  .card--front-one .info__divider{width:278px;margin-top:17px}
  .card--front-one .info__lic{margin-top:18px}

  .card--front-two .info{top:75px}
  .card--front-two .info__name{color:var(--green)}
  .card--front-two .info__title{color:var(--white)}
  .card--front-two .info__divider{width:19px;margin-top:16px}
  .card--front-two .info__lic{margin-top:18px}

  .brand-foot{position:absolute;left:0;right:0;bottom:0;height:198px;background:var(--ink);
    display:flex;align-items:center;justify-content:center}
  .brand-foot__name{font-weight:900;font-size:24px;letter-spacing:2px;line-height:1.25;color:var(--green);text-align:center;text-transform:uppercase}

  .back__established{position:absolute;top:140px;width:66px;text-align:center;
    font-size:14px;font-weight:700;letter-spacing:4px;color:var(--white);
    border-top:1.5px solid var(--green);border-bottom:1.5px solid var(--green);padding:6px 0 5px}
  .back__established--left{left:103px}
  .back__established--right{right:100px}
  .back__mark{position:absolute;left:0;right:0;top:113px;display:flex;justify-content:center}
  .back__mark span{width:60px;height:60px;background:var(--green);display:block}
  .back__name{position:absolute;left:0;right:0;top:198px;text-align:center;
    font-weight:900;font-size:34px;letter-spacing:3px;line-height:1.15;color:var(--white);text-transform:uppercase}

  .label{position:absolute;width:360px;text-align:center;font-weight:900;font-size:21px;color:#000;line-height:1}
  .label--front-one{left:214px;top:710px}
  .label--front-two{left:626px;top:710px}
  .label--back{left:420px;top:1126px}
</style>
</head>
<body>

<svg width="0" height="0" style="position:absolute" aria-hidden="true">
  <defs>
    <symbol id="icon-phone" viewBox="0 0 26 26">
      <circle cx="13" cy="13" r="13" fill="#70b548"/>
      <path d="M9 7.5c.6-.4 1.2-.2 1.5.3l1.2 2c.3.5.2 1-.2 1.4l-.8.7c.6 1.4 1.6 2.5 3 3.2l.7-.8c.4-.4.9-.5 1.4-.2l2 1.2c.5.3.7 1 .3 1.5l-.8 1c-.6.7-1.6.9-2.5.5-3-1.3-5.300-3.6-6.5-6.6-.4-.9-.1-1.9.6-2.5z" fill="#231f20"/>
      <path d="M14.5 8.5a4 4 0 0 1 3.2 3.2M14.5 6a6.5 6.5 0 0 1 5.7 5.7" stroke="#231f20" stroke-width="1.2" fill="none" stroke-linecap="round"/>
    </symbol>
    <symbol id="icon-mail" viewBox="0 0 26 26">
      <circle cx="13" cy="13" r="13" fill="#70b548"/>
      <rect x="7" y="9" width="12" height="8.5" fill="none" stroke="#231f20" stroke-width="1.2"/>
      <path d="M7 9l6 5 6-5M7 17.5l4.5-4M19 17.5l-4.5-4" stroke="#231f20" stroke-width="1.1" fill="none"/>
    </symbol>
    <symbol id="icon-pin" viewBox="0 0 26 26">
      <circle cx="13" cy="13" r="13" fill="#70b548"/>
      <path d="M13 6.5a4.3 4.3 0 0 0-4.3 4.3c0 3.2 4.3 8.2 4.3 8.2s4.3-5 4.3-8.2A4.3 4.3 0 0 0 13 6.5z" fill="#231f20"/>
      <circle cx="13" cy="10.8" r="1.6" fill="#70b548"/>
    </symbol>
  </defs>
</svg>

<section class="card card--front-one">
  <div class="hero-band">
    <div class="hero-band__name">Brennick<br>Framing Company</div>
  </div>
  <div class="info">
    <h1 class="info__name">Marcus Brennick</h1>
    <p class="info__title">Owner/Project Manager</p>
    <div class="info__icons">
      <span class="info__rule"></span>
      <svg><use href="#icon-phone"/></svg>
      <svg><use href="#icon-mail"/></svg>
      <svg><use href="#icon-pin"/></svg>
      <span class="info__rule"></span>
    </div>
    <p class="info__phone">647.382.9105</p>
    <p class="info__line">brennickframingcompany@quillpost.example</p>
    <p class="info__line">418 Larkspur Ln, Alder Bay, OR 97999</p>
    <div class="info__divider"></div>
    <p class="info__lic">Lic# 5836214</p>
  </div>
</section>

<section class="card card--front-two">
  <div class="info">
    <h1 class="info__name">Marcus Brennick</h1>
    <p class="info__title">Owner/Project Manager</p>
    <div class="info__icons">
      <span class="info__rule"></span>
      <svg><use href="#icon-phone"/></svg>
      <svg><use href="#icon-mail"/></svg>
      <svg><use href="#icon-pin"/></svg>
      <span class="info__rule"></span>
    </div>
    <p class="info__phone">647.382.9105</p>
    <p class="info__line">brennickframingcompany@quillpost.example</p>
    <p class="info__line">418 Larkspur Ln, Alder Bay, OR 97999</p>
    <div class="info__divider"></div>
    <p class="info__lic">Lic# 5836214</p>
  </div>
  <div class="brand-foot">
    <div class="brand-foot__name">Brennick<br>Framing Company</div>
  </div>
</section>

<section class="card card--back">
  <div class="back__established back__established--left">ESTD</div>
  <div class="back__mark"><span></span></div>
  <div class="back__established back__established--right">2020</div>
  <div class="back__name">Brennick<br>Framing Company</div>
</section>

<p class="label label--front-one">FRONT 01</p>
<p class="label label--front-two">FRONT 02</p>
<p class="label label--back">BACK</p>

</body>
</html>
```